Yard Sign

8.5 inch x 11 inch (landscape orientation) Yard sign advertising:

Solar Patios and Structures

Info required on sign:
address - 4716 Marlow Avenue Suite B, Bakersfield, CA 93301

contact info - info@varnel-group.com
web - www.varnel-group.com
toll free - 877.555.0194
local - 661.555.0148

```html
<!DOCTYPE html>
<html lang="en">
<head>
<meta charset="utf-8">
<title>Varnel Group — Solar Patios and Structures Yard Sign</title>
<link rel="stylesheet" href="https://fonts.googleapis.com/css2?family=Arimo:wght@400;700&family=Oswald:wght@700&display=swap">
<style>
  :root {
    --navy: #1c3f73;
    --orange: #e8792b;
    --white: #ffffff;
    --page: #f1f1f1;
  }
  html, body {
    margin: 0;
    width: 1200px;
    height: 900px;
    overflow: hidden;
    background: var(--page);
  }
  .yard-sign {
    position: absolute;
    left: 25px;
    top: 5px;
    width: 1150px;
    height: 889px;
    display: block;
  }
  .headline { font-family: "Arimo", Arial, sans-serif; font-weight: 700; fill: var(--white); }
  .headline-joiner { font-family: "Arimo", Arial, sans-serif; font-weight: 400; fill: var(--orange); }
  .address { font-family: "Arimo", Arial, sans-serif; fill: var(--white); }
  .contact-strong { font-family: "Oswald", Impact, sans-serif; font-weight: 700; }
  .brand-name { font-family: "Arimo", Arial, sans-serif; font-weight: 700; fill: var(--navy); }
</style>
</head>
<body>
<svg class="yard-sign" viewBox="0 0 1623 1254" xmlns="http://www.w3.org/2000/svg">
  <defs>
    <linearGradient id="scene-tones" x1="0" y1="0" x2="0" y2="1">
      <stop offset="0" stop-color="#6f9fd0"/>
      <stop offset="0.3" stop-color="#a8c3de"/>
      <stop offset="0.5" stop-color="#6a7f99"/>
      <stop offset="0.6" stop-color="#4a5a6e"/>
      <stop offset="0.64" stop-color="#3c57b0"/>
      <stop offset="1" stop-color="#2b3f9e"/>
    </linearGradient>
    <filter id="text-lift" x="-5%" y="-20%" width="110%" height="140%">
      <feDropShadow dx="2" dy="3" stdDeviation="1.5" flood-color="#000" flood-opacity="0.55"/>
    </filter>
  </defs>

  <!-- rooftop solar scene -->
  <rect class="scene-photo" x="0" y="0" width="1000" height="1254" fill="url(#scene-tones)" role="img" aria-label="City skyline behind a rooftop array of blue solar panels"/>

  <!-- brand band -->
  <polygon class="brand-band" points="0,118 770,118 800,301 0,301" fill="var(--white)" fill-opacity="0.6"/>
  <text class="brand-name" x="150" y="232" font-size="74">Varnel Group</text>
  <circle class="brand-mark" cx="680" cy="207" r="52" fill="var(--orange)"/>

  <!-- main blue panel -->
  <polygon class="info-panel" points="1100,0 1623,0 1623,1254 948,1254 693,385 740,330" fill="var(--navy)"/>
  <polygon class="accent-triangle" points="701,0 1100,0 810,382" fill="var(--orange)"/>
  <polygon class="accent-corner" points="833,1254 923,1147 948,1254" fill="var(--orange)"/>

  <!-- headline -->
  <g filter="url(#text-lift)">
    <text class="headline" x="923" y="392" font-size="74" textLength="595" lengthAdjust="spacing">SOLAR PATIOS</text>
    <text class="headline-joiner" x="1208" y="477" font-size="72" text-anchor="middle">and</text>
    <text class="headline" x="955" y="567" font-size="74" textLength="533" lengthAdjust="spacing">STRUCTURES</text>
  </g>

  <!-- address -->
  <g class="pin-icon" transform="translate(968,732)">
    <path d="M0,-30 a22,22 0 0 1 22,22 c0,18 -22,40 -22,40 c0,0 -22,-22 -22,-40 a22,22 0 0 1 22,-22z" fill="var(--white)"/>
    <circle cx="0" cy="-8" r="10" fill="var(--navy)"/>
    <circle cx="0" cy="-8" r="6" fill="var(--white)"/>
  </g>
  <g filter="url(#text-lift)">
    <text class="address" x="1038" y="732" font-size="35" textLength="455" lengthAdjust="spacingAndGlyphs">4716 Marlow Avenue Suite B,</text>
    <text class="address" x="1038" y="782" font-size="35">Bakersfield, CA 93301</text>
  </g>

  <!-- phone -->
  <g class="phone-icon" transform="translate(970,932)" fill="var(--white)">
    <path d="M-26,-10 q26,-20 52,0 l-4,10 h-10 l-2,-6 q-10,-4 -20,0 l-2,6 h-10z"/>
    <path d="M-14,0 h28 l8,20 h-44z"/>
    <circle cx="0" cy="11" r="6" fill="var(--navy)"/>
  </g>
  <g filter="url(#text-lift)">
    <text class="contact-strong" x="1038" y="948" font-size="54" fill="var(--white)" textLength="317" lengthAdjust="spacingAndGlyphs">877.555.0194</text>
    <text class="contact-strong" x="1038" y="1020" font-size="54" fill="var(--white)" textLength="317" lengthAdjust="spacingAndGlyphs">661.555.0148</text>
  </g>

  <!-- web band -->
  <polygon class="web-band" points="0,1053 893,1053 920,1167 0,1167" fill="var(--white)"/>
  <g class="globe-icon" transform="translate(172,1117)" fill="none" stroke="var(--navy)" stroke-width="4">
    <circle r="20"/>
    <ellipse rx="9" ry="20"/>
    <line x1="-20" y1="0" x2="20" y2="0"/>
  </g>
  <text class="contact-strong" x="228" y="1132" font-size="50" fill="var(--navy)" textLength="518" lengthAdjust="spacingAndGlyphs">www.varnel-group.com</text>

  <!-- email band -->
  <polygon class="email-band" points="893,1055 1623,1055 1623,1169 923,1169" fill="var(--orange)"/>
  <text class="contact-strong" x="968" y="1132" font-size="50" fill="var(--white)" textLength="518" lengthAdjust="spacingAndGlyphs" filter="url(#text-lift)">info@varnel-group.com</text>
</svg>
</body>
</html>
```